Business Card Design for Kind Helper

I am starting my own consultancy business, using what I learned in marketing and advertising to help Non -profits with marketing and communications needs. I need a professional business card design to hand out to my clients.

My business name is “Outreach2Kindness” my vision is that this need this to be reflective of marketing doing good for the world through the power of communications. I like the color palettes in olives, creams and oranges but am open to design options.
In addition to the cards I am asking for separate file for the logo and will need a JPG, PSD Vector File.

Information to go on the card:

Morwenna Calloway
Marketing Consultant
Email: outreach2kindness@mailbrook.com, callowaym1@brinmoreu.edu
Website: Outreach2Kindness.com

Communications

```html
<!DOCTYPE html>
<html lang="en">
<head>
<meta charset="utf-8">
<title>Outreach2Kindness – Business Card Options</title>
<link href="https://fonts.googleapis.com/css2?family=Arimo:wght@400;700&display=swap" rel="stylesheet">
<style>
  :root {
    --page: #ffffff;
    --card: #efeff1;
    --card-alt: #f6f7f9;
    --card-border: #d6d8dc;
    --teal: #4a717f;
    --ink: #4a4a4a;
    --ink-dark: #3a3a3a;
    --white: #ffffff;
    --rule-maroon: #7a3a43;
    --rule-teal: #4f7689;
  }
  * { box-sizing: border-box; margin: 0; padding: 0; }
  html, body {
    width: 1200px;
    height: 692px;
    overflow: hidden;
    background: var(--page);
    font-family: "Arimo", Arial, sans-serif;
  }
  .sheet { position: relative; width: 1200px; height: 692px; }

  .option-number {
    position: absolute;
    left: 26px;
    font-size: 15px;
    color: var(--ink-dark);
  }
  .option-number.first { top: 30px; }
  .option-number.second { top: 390px; }

  .card {
    position: absolute;
    width: 524px;
    height: 280px;
    background: var(--card);
    overflow: hidden;
  }
  .card.front { left: 52px; }
  .card.back { left: 652px; }
  .row-one { top: 36px; }
  .row-two { top: 386px; }
  .card.front.alt {
    background: var(--card-alt);
    border: 1px solid var(--card-border);
  }

  /* Front: brand name */
  .brand-dot {
    position: absolute;
    left: 226px;
    top: 62px;
    width: 72px;
    height: 72px;
    border-radius: 50%;
    background: var(--teal);
  }
  .brand-name {
    position: absolute;
    left: 0;
    right: 0;
    top: 214px;
    text-align: center;
    font-size: 42px;
    font-weight: 700;
    letter-spacing: -0.5px;
    color: var(--ink);
  }

  /* Back */
  .back-panel {
    position: absolute;
    left: 0;
    top: 0;
    width: 100%;
    height: 100%;
    background: var(--teal);
    clip-path: polygon(0 0, 132px 0, 264px 100%, 0 100%);
  }
  .contact-emails {
    position: absolute;
    right: 46px;
    top: 42px;
    text-align: right;
    font-size: 18px;
    line-height: 24px;
    color: var(--ink-dark);
  }
  .side-rule {
    position: absolute;
    left: 486px;
    top: 22px;
    width: 2px;
    height: 264px;
  }
  .row-one .side-rule { background: var(--rule-maroon); }
  .row-two .side-rule { background: var(--rule-teal); }

  .person {
    position: absolute;
    left: 16px;
    top: 126px;
    color: var(--white);
    font-size: 16px;
    line-height: 22px;
  }
  .person-name { font-weight: 700; }
  .row-two .person { top: 136px; }

  .website {
    position: absolute;
    left: 28px;
    top: 234px;
    font-size: 22px;
    font-weight: 700;
    color: var(--white);
  }
  .website .domain { color: var(--teal); }
</style>
</head>
<body>
<main class="sheet">
  <span class="option-number first">1</span>
  <span class="option-number second">2</span>

  <!-- Option 1 -->
  <section class="card front row-one">
    <span class="brand-dot"></span>
    <p class="brand-name">Outreach2Kindness</p>
  </section>
  <section class="card back row-one">
    <div class="back-panel"></div>
    <div class="contact-emails">
      <p>outreach2kindness@mailbrook.com</p>
      <p>callowaym1@brinmoreu.edu</p>
    </div>
    <span class="side-rule"></span>
    <div class="person">
      <p class="person-name">Morwenna Calloway</p>
      <p class="person-title">Marketing Consultant</p>
    </div>
    <p class="website">Outreach2Kindness<span class="domain">.com</span></p>
  </section>

  <!-- Option 2 -->
  <section class="card front alt row-two">
    <span class="brand-dot"></span>
    <p class="brand-name">Outreach2Kindness</p>
  </section>
  <section class="card back row-two">
    <div class="back-panel"></div>
    <div class="contact-emails">
      <p>outreach2kindness@mailbrook.com</p>
      <p>callowaym1@brinmoreu.edu</p>
    </div>
    <span class="side-rule"></span>
    <div class="person">
      <p class="person-name">Morwenna Calloway</p>
      <p class="person-title">Marketing Consultant</p>
    </div>
    <p class="website">Outreach2Kindness<span class="domain">.com</span></p>
  </section>
</main>
</body>
</html>
```